Metal Fabrication Business Cards

We need a business card for our business of Metal Fabrication/Welding. Our company is called "Hadley's Metal Fabrication"

We are a metal fabrication business which takes on "high class" clients- dealing with some of the biggest builders in Australia. Our work is neat, and the type of work we do is 2nd to none for quality. We want to show that on our cards. However, we would love to show a side that is down to earth and a bit more modern and contemporary - we are all young in business so would love to show that side - rather than a boring "very straight looking" card. We always have a clean workshop and take pride in our presentation. We want to come across like we are very rich, but would love to go for a surf as well! A card that basically says we have high class and will charge you a high rate - but the quality will be outstanding.

Front of card: - Simply but sharp!
-Thinking maybe white card - with nice black writing.
-On the right hand side of card a person welding - or holding a welder.
- My business name - Hadley's Metal Fabrication
-Also maybe my name - which is 'Corey" (if it doesn't work, we can put this on the back of card.)
- if needed to look better - we can put keywords on front of card like "metal fabrication, sheet metal, welding etc" but I dont want it to be crowded.

Back of card: - Also make smart but sharp!
Put details such as:
04387 21 914
hadley.fabrication@tinmailbox.com.au
7/32 Keel Street
North Corvale NSW 2471
www.korvinfabrication.com.au
ABN 72 615 803 914

thats just an idea - its now up to you. I don't mind what you come up with - as long as it stands out from the rest and looks sharp, professional but contemporary.

Business

Put details such as:
04387 21 914
7/32 Keel Street
North Corvale NSW 2471
ABN 72 615 803 914

Hadley's Metal Fabrication

```html
<!DOCTYPE html>
<html lang="en">
<head>
<meta charset="utf-8">
<title>Hadley's Metal Fabrication – Business Cards</title>
<link rel="stylesheet" href="https://fonts.googleapis.com/css2?family=Merienda:wght@500;700&family=Arimo:wght@400&family=Tinos:wght@400&display=swap">
<style>
  :root {
    --bg-top: #8f8f8f;
    --bg-bottom: #cfcfcf;
    --card: #f4f4f4;
    --ink: #2f2f2f;
    --ink-green: #3d4a40;
    --ink-soft: #6a6a6a;
    --rule: #2b3a2f;
  }
  * { margin: 0; padding: 0; box-sizing: border-box; }
  html, body {
    width: 1200px;
    height: 1200px;
    overflow: hidden;
  }
  body {
    background: linear-gradient(180deg, var(--bg-top) 0%, var(--bg-bottom) 100%);
    position: relative;
  }
  .card {
    position: absolute;
    left: 150px;
    width: 900px;
    height: 514px;
    background: var(--card);
    box-shadow: 0 6px 18px rgba(0,0,0,0.18);
  }
  .card--front { top: 50px; }
  .card--back { top: 636px; }

  .front__name {
    position: absolute;
    top: 170px;
    left: 0;
    width: 100%;
    text-align: center;
    font-family: "Merienda", cursive;
    font-weight: 700;
    font-size: 46px;
    letter-spacing: 1px;
    color: var(--ink);
  }
  .front__tagline {
    position: absolute;
    top: 310px;
    left: 0;
    width: 100%;
    text-align: center;
    font-family: "Tinos", serif;
    font-size: 24px;
    letter-spacing: 1px;
    color: var(--ink-soft);
  }

  .back__name {
    position: absolute;
    top: 70px;
    left: 40px;
    width: 450px;
    font-family: "Merienda", cursive;
    font-weight: 500;
    font-size: 27px;
    color: var(--ink-green);
    white-space: nowrap;
  }
  .back__rule {
    position: absolute;
    left: 510px;
    top: 40px;
    width: 2px;
    height: 420px;
    background: var(--rule);
  }
  .back__details {
    position: absolute;
    left: 532px;
    top: 282px;
    list-style: none;
    font-family: "Arimo", sans-serif;
    font-size: 17px;
    line-height: 1.25;
    color: var(--ink);
    white-space: nowrap;
  }
</style>
</head>
<body>
  <section class="card card--front" aria-label="Card front">
    <h1 class="front__name">Hadley's Metal Fabrication</h1>
    <p class="front__tagline">"metal fabrication, sheet metal, welding"</p>
  </section>

  <section class="card card--back" aria-label="Card back">
    <h2 class="back__name">Hadley's Metal Fabrication</h2>
    <div class="back__rule"></div>
    <ul class="back__details">
      <li>04387 21 914</li>
      <li>hadley.fabrication@tinmailbox.com.au</li>
      <li>www.korvinfabrication.com.au</li>
      <li>7/32 Keel Street North Corvale NSW 2471</li>
      <li>ABN 72 615 803 914</li>
    </ul>
  </section>
</body>
</html>
```